Marta Quinlan Photography needs a unique, creative business card/logo design

I need a design for business cards/logo that is unique and creative in the industry. Simplicity is nice, so not too crowded. Something that will catch my customer's eye and remain in their memory. I am primarily a landscape photographer but will be soon may be branching into boudoir photography as well. I have attached my current card.

Industry/Entity Type

Business

Contact Information for Business Card

Marta Quinlan Photography
Phone: 0439 271 504
Email: MartaQuinlanPhotography@brivomail.net
Website: www.pagerly.net/MartaQuinlanPhotography.Aust

Logo Text

Marta Quinlan Photography

Requirements
Must have
• Contact Details on one side
Should not have
• pixelation

```html
<!DOCTYPE html>
<html lang="en">
<head>
<meta charset="utf-8">
<title>Marta Quinlan Photography — Business Card</title>
<link rel="stylesheet" href="https://fonts.googleapis.com/css2?family=Questrial&display=swap">
<style>
  :root {
    --backdrop: #ebebeb;
    --card: #232323;
    --gold: #a6773a;
  }
  * { margin: 0; padding: 0; box-sizing: border-box; }
  html, body {
    width: 952px;
    height: 1200px;
    overflow: hidden;
    background: var(--backdrop);
    font-family: "Questrial", sans-serif;
  }
  .canvas { position: relative; width: 952px; height: 1200px; }
  .card {
    position: absolute;
    left: 96px;
    width: 760px;
    height: 428px;
    background: var(--card);
    color: var(--gold);
  }
  .card--front { top: 120px; }
  .card--back { top: 652px; }
  .frame { position: absolute; inset: 0; width: 100%; height: 100%; }
  .frame path { fill: none; stroke: var(--gold); stroke-width: 3.5; }

  .brand {
    position: absolute;
    left: 0; right: 0;
    top: 160px;
    text-align: center;
  }
  .brand__name {
    display: block;
    font-size: 54px;
    line-height: 1;
    letter-spacing: 1px;
    margin-left: 28px;
  }
  .brand__tagline {
    display: block;
    margin-top: 22px;
    margin-left: 28px;
    font-size: 19px;
    letter-spacing: 7px;
  }

  .contact {
    position: absolute;
    left: 0; right: 0;
    text-align: center;
    font-size: 14.5px;
    letter-spacing: 2.6px;
    white-space: nowrap;
  }
  .contact-icon {
    position: absolute;
    left: 351px;
    width: 60px;
    height: 60px;
  }
  .contact-icon circle { fill: none; stroke: var(--gold); stroke-width: 2.5; }
  .contact-icon .glyph-line { fill: none; stroke: var(--gold); stroke-width: 3.5; stroke-linecap: round; }
  .contact-icon .glyph-fill { fill: var(--gold); }
  .contact-icon .glyph-cut { fill: none; stroke: var(--card); stroke-width: 1.6; }
</style>
</head>
<body>
<main class="canvas">

  <section class="card card--front" aria-label="Card front">
    <svg class="frame" viewBox="0 0 760 428" aria-hidden="true">
      <path d="M22 81 V24 H97"/>
      <path d="M663 24 H738 V81"/>
      <path d="M22 347 V404 H97"/>
      <path d="M663 404 H738 V347"/>
      <path d="M0 219 H76"/>
      <path d="M684 219 H760"/>
    </svg>
    <h1 class="brand">
      <span class="brand__name">Marta Quinlan</span>
      <span class="brand__tagline">PHOTOGRAPHY</span>
    </h1>
  </section>

  <section class="card card--back" aria-label="Card back with contact details">
    <svg class="frame" viewBox="0 0 760 428" aria-hidden="true">
      <path d="M22 81 V24 H97"/>
      <path d="M663 24 H738 V81"/>
      <path d="M22 347 V404 H97"/>
      <path d="M663 404 H738 V347"/>
      <path d="M0 216 H76"/>
      <path d="M684 216 H760"/>
    </svg>

    <svg class="contact-icon" style="top:51px" viewBox="0 0 60 60" aria-hidden="true">
      <circle cx="30" cy="30" r="28"/>
      <g transform="rotate(-45 30 30)">
        <rect class="glyph-line" x="14" y="25" width="18" height="10" rx="5"/>
        <rect class="glyph-line" x="28" y="25" width="18" height="10" rx="5"/>
      </g>
    </svg>
    <p class="contact contact--web" style="top:124px">www.pagerly.net/MartaQuinlanPhotography.Aust</p>

    <svg class="contact-icon" style="top:160px" viewBox="0 0 60 60" aria-hidden="true">
      <circle cx="30" cy="30" r="28"/>
      <path class="glyph-fill" d="M19 16c2-2 4-2 5 0l3 5c1 2 0 3-1 4l-2 2c1 4 5 8 9 10l2-2c1-1 3-2 4-1l5 3c2 1 2 3 0 5l-2 2c-3 3-9 1-15-5s-9-12-6-16z"/>
    </svg>
    <p class="contact contact--phone" style="top:250px">0439 271 504</p>

    <svg class="contact-icon" style="top:275px" viewBox="0 0 60 60" aria-hidden="true">
      <circle cx="30" cy="30" r="28"/>
      <path class="glyph-fill" d="M15 26 L30 14 L45 26 V44 H15 Z"/>
      <path class="glyph-cut" d="M15 26 L30 37 L45 26 M15 44 L26 34 M45 44 L34 34"/>
    </svg>
    <p class="contact contact--email" style="top:355px">MartaQuinlanPhotography@brivomail.net</p>
  </section>

</main>
</body>
</html>
```